Vero-Shine Janitorial Services

Looking for a modern design for my new business. I like the clear see through of the card I've attached. The business is built around The Brightwell Omni 720 system, with that said I'd like to add the brightwell logo on the bachside with the statement of Powered by (then the Brightwell Logo). I really like the layout and color schemes of the card I attached. Black, Blue, and White. I would like to incorporate three images into the diamond shape, as seem in the layout.

Martin Okafor
Managing Partner

Still waiting on revisions?

```html
<!DOCTYPE html>
<html lang="en">
<head>
<meta charset="utf-8">
<title>Vero-Shine Janitorial Services — Business Card</title>
<link rel="stylesheet" href="https://fonts.googleapis.com/css2?family=Marcellus&family=Montserrat:wght@400;500;700&display=swap">
<style>
  :root {
    --page: #ececec;
    --charcoal-dark: #303030;
    --charcoal-light: #474747;
    --brand-blue: #1070bb;
    --frame-blue: #1a66b3;
    --sky-blue: #3c9fdb;
    --wordmark-grey: #7d848c;
    --ink: #232323;
    --muted: #6b6f75;
    --white: #ffffff;
  }
  * { margin: 0; padding: 0; box-sizing: border-box; }
  html, body { width: 1200px; height: 1200px; overflow: hidden; }
  body { background: var(--page); position: relative; font-family: "Montserrat", sans-serif; }

  .card { position: absolute; left: 280px; width: 640px; height: 366px; overflow: hidden; }

  /* Front */
  .card-front {
    top: 130px;
    background: linear-gradient(200deg, var(--charcoal-light) 0%, var(--charcoal-dark) 55%, #2e2e2e 100%);
  }
  .brand-mark {
    position: absolute; left: 50%; top: 100px; width: 110px; height: 110px;
    transform: translateX(-50%); border-radius: 50%; background: var(--sky-blue);
  }
  .brand-name {
    position: absolute; left: 0; right: 0; top: 218px; text-align: center;
    font-family: "Marcellus", serif; color: var(--wordmark-grey);
    font-size: 34px; letter-spacing: 2px; line-height: 1;
  }
  .brand-sub {
    position: absolute; left: 0; right: 0; top: 255px; text-align: center;
    font-family: "Marcellus", serif; color: var(--wordmark-grey);
    font-size: 13px; letter-spacing: 1.6px; line-height: 1;
  }

  /* Back */
  .card-back { top: 604px; background: var(--white); }
  .photo-diamonds { position: absolute; left: 0; top: 0; width: 260px; height: 366px; }
  .accent-band {
    position: absolute; left: 273px; top: 0; width: 40px; height: 366px;
    background: var(--brand-blue); border-radius: 0 0 20px 20px;
  }
  .contact-icon {
    position: absolute; left: 278px; width: 30px; height: 30px; border-radius: 50%;
    background: var(--white); display: flex; align-items: center; justify-content: center;
  }
  .contact-icon svg { width: 16px; height: 16px; }
  .contact-text {
    position: absolute; left: 319px; font-size: 14.5px; font-weight: 500;
    color: var(--ink); letter-spacing: 0.3px; line-height: 1;
  }
  .person-name {
    position: absolute; left: 322px; top: 146px; font-size: 29px; font-weight: 700;
    color: var(--brand-blue); letter-spacing: 0.5px; line-height: 1;
  }
  .person-role {
    position: absolute; left: 323px; top: 182px; font-size: 16px; font-weight: 500;
    color: var(--brand-blue); letter-spacing: 0.4px; line-height: 1;
  }
  .partner-lockup {
    position: absolute; right: 28px; top: 22px; height: 60px;
    display: flex; align-items: center; gap: 12px;
  }
  .partner-text { display: flex; flex-direction: column; align-items: flex-end; gap: 4px; }
  .powered-by {
    font-size: 10px; font-weight: 500; color: var(--muted);
    letter-spacing: 0.6px; line-height: 1;
  }
  .partner-name {
    font-size: 19px; font-weight: 700; color: var(--brand-blue); line-height: 1;
  }
  .partner-badge {
    flex: none; width: 60px; height: 60px;
    border-radius: 50%; border: 3px solid var(--brand-blue);
  }
</style>
</head>
<body>

  <section class="card card-front" aria-label="Card front">
    <div class="brand-mark"></div>
    <div class="brand-name">Vero-Shine</div>
    <div class="brand-sub">Janitorial Services</div>
  </section>

  <section class="card card-back" aria-label="Card back">
    <svg class="photo-diamonds" viewBox="0 0 260 366">
      <defs>
        <linearGradient id="cleaner-tones" x1="0" y1="0" x2="1" y2="1">
          <stop offset="0" stop-color="#8b9097"/>
          <stop offset="1" stop-color="#c9ccd1"/>
        </linearGradient>
        <linearGradient id="mop-tones" x1="0" y1="0" x2="1" y2="1">
          <stop offset="0" stop-color="#6f7277"/>
          <stop offset="0.6" stop-color="#d9c237"/>
          <stop offset="1" stop-color="#c4c7cb"/>
        </linearGradient>
        <radialGradient id="system-tones" cx="0.5" cy="0.4" r="0.6">
          <stop offset="0" stop-color="#e4f1fb"/>
          <stop offset="1" stop-color="#2a78c6"/>
        </radialGradient>
      </defs>
      <polygon role="img" aria-label="Photo of a cleaner using the spraying system" points="69,86 124,141 69,196 14,141" fill="url(#cleaner-tones)" stroke="var(--frame-blue)" stroke-width="3"/>
      <polygon role="img" aria-label="Photo of a yellow mop bucket on a shiny floor" points="184,86 239,141 184,196 129,141" fill="url(#mop-tones)" stroke="var(--frame-blue)" stroke-width="3"/>
      <polygon role="img" aria-label="Product photo of the Brightwell Omni 720 system" points="126,142 196,212 126,282 56,212" fill="url(#system-tones)" stroke="var(--frame-blue)" stroke-width="3"/>
    </svg>

    <div class="partner-lockup">
      <div class="partner-text">
        <span class="powered-by">Powered by</span>
        <span class="partner-name">Brightwell</span>
      </div>
      <div class="partner-badge"></div>
    </div>

    <div class="person-name">MARTIN OKAFOR</div>
    <div class="person-role">MANAGING PARTNER</div>

    <div class="accent-band"></div>

    <div class="contact-icon" style="top:228px" aria-hidden="true">
      <svg viewBox="0 0 16 16"><path d="M2 5c0-2 3-3 6-3s6 1 6 3v1h-3V5H5v1H2z M4 7h8l1 6H3z" fill="var(--brand-blue)"/><circle cx="8" cy="10" r="1.6" fill="#fff"/></svg>
    </div>
    <div class="contact-text" style="top:236px">077 5550192</div>

    <div class="contact-icon" style="top:272px" aria-hidden="true">
      <svg viewBox="0 0 16 16"><rect x="1.5" y="3.5" width="13" height="9" fill="none" stroke="var(--brand-blue)" stroke-width="1.5"/><path d="M1.5 3.5l6.5 5 6.5-5M1.5 12.5l5-4.5M14.5 12.5l-5-4.5" fill="none" stroke="var(--brand-blue)" stroke-width="1.3"/></svg>
    </div>
    <div class="contact-text" style="top:280px">admin@veroshinemgmt.com</div>

    <div class="contact-icon" style="top:317px" aria-hidden="true">
      <svg viewBox="0 0 16 16"><circle cx="8" cy="8" r="6.5" fill="none" stroke="var(--brand-blue)" stroke-width="1.4"/><ellipse cx="8" cy="8" rx="3" ry="6.5" fill="none" stroke="var(--brand-blue)" stroke-width="1.2"/><path d="M1.5 8h13M2.5 5h11M2.5 11h11" stroke="var(--brand-blue)" stroke-width="1.1"/></svg>
    </div>
    <div class="contact-text" style="top:325px">www.vsmgmt.com</div>
  </section>

</body>
</html>
```